Vela Errands Web Design Project

Homepage components
o Logo
o Rotating header
o Main menu
o Animation video
o Banners
o Members login
o Latest news

The design’s preferred colors are black (background), silver (main tabs) and white (text)

Site map:
• Home
• News
• About us
o Welcome Note
o Company Profile
• Member Log in
o Registered homepage
? Request a service (form)
? Services directory
? Update profile
? Services history
• Member registration
o Registration form
• Partners
Footer Menu
• Contact us
• Terms & Conditions
• Privacy policy
• Social media links
• Sitemap

Brief about the company:
Vela Errands is a Jordanian company dedicated to elevate and redefine the level of service in the country. We are set out to give premium services at affordable prices. In this fast paced environment that we live in, we barely have the luxury of free time anymore and we, at Vela Errands will be giving you that extra hour or two per day to spend as your heart desires!
By becoming a member you will get access to a world of comfort and peace of mind. We have done the homework on your behalf and have established the network of connections that will enable you to live a headache free life.
We will be providing our members with support and assistance in their day to day lives in the fields that consumes and wastes time the most. We are value driven and below is our “ever-growing” list of services that we will provide at excellent prices:
• Maintenance (carpentry, plumbing, electrical, painting, decorating, gardening… etc)
• Cleaning (pre and post tenancy, periodical deep cleaning, packing and moving services, laundry… etc)
• Personalized delivery services (grocery, important documents, office related supplies, posting cheques, food, paying bills… etc)
• Passport, driving license and ID reissuance
• Travel arrangements (flights, hotels, airport transfers… etc)
• Premium car rental services
• Restaurant reservations
• IT assistance
• Event planning and all related services
• Catering arrangements

Aside from all the services we have on offer we have collaborated with a number of places (that we like to call partners) in town where Vela Errands members are entitled to benefits and privileges that will most certainly add value to their membership. Alongside our partners we have come up with the best formula that will please our members. Below are some of our current partners:

Requirements
Must have
• Homepage components
o Logo
o Rotating header
o Main menu
o Animation video
o Banners
o Members login
o Latest news

```html
<!DOCTYPE html>
<html lang="en">
<head>
<meta charset="utf-8">
<title>Vela Errands – Home</title>
<link rel="stylesheet" href="https://fonts.googleapis.com/css2?family=Open+Sans:wght@400;600;700&family=Didact+Gothic&display=swap">
<style>
:root{
  --ink:#111;
  --text:#222;
  --muted:#444;
  --silver:#e6e6e6;
  --orange-light:#f29b1c;
  --orange-dark:#d97206;
  --footer:#363636;
  --footer-base:#2b2b2b;
  --footer-text:#9a9a9a;
  --white:#fff;
}
*{margin:0;padding:0;box-sizing:border-box}
html,body{width:863px;height:1200px;overflow:hidden;background:var(--white)}
body{position:relative;font-family:"Open Sans",Arial,sans-serif;color:var(--text)}
.abs{position:absolute}
.heading{font-family:"Didact Gothic","Century Gothic",sans-serif;color:var(--ink);font-weight:400}

/* header */
.top-strip{left:0;top:0;width:863px;height:5px;background:#dcdcdc}
.header{left:0;top:5px;width:863px;height:117px;background:linear-gradient(#fff 40%,#ececec)}
.member-label{left:656px;top:15px;font-size:10.5px;font-weight:600;color:#222}
.member-btn{top:11px;height:21px;border:1px solid #b5b5b5;border-radius:3px;background:linear-gradient(#f4f4f4,#d6d6d6);font-size:10.5px;color:#444;display:flex;align-items:center;justify-content:center}
.logo{left:27px;top:50px}
.logo-name{font-size:30px;font-weight:400;color:#2a2a2a;letter-spacing:.5px;line-height:1}
.logo-tag{font-size:9px;color:#888;margin-top:3px;margin-left:2px}
.nav a{position:absolute;top:74px;height:22px;line-height:22px;font-size:12.5px;color:#111;text-decoration:none}
.nav a.active{background:#0d0d0d;color:#fff;border-radius:3px;width:66px;text-align:center}

/* banner */
.ad-banner{left:215px;top:129px;width:614px;height:77px;border:1px solid #bbb;background:#fff}
.ad-fill{position:absolute;left:1px;top:1px;width:393px;height:73px;background:linear-gradient(90deg,#1d7fd2,#3a9be0 55%,#e8f3fb)}

/* hero */
.hero-photo{left:21px;top:218px;width:582px;height:230px;background:linear-gradient(135deg,#3b3128,#1d1a18 45%,#4a3e33)}
.featured{left:603px;top:218px;width:230px;height:230px;background:linear-gradient(90deg,var(--orange-light),var(--orange-dark));border-radius:0 3px 3px 0}
.featured h2{position:absolute;left:25px;top:13px;font-size:22px;font-weight:600;color:#fff}
.featured ul{position:absolute;left:25px;top:54px;list-style:none;width:190px}
.featured li{height:25.3px;line-height:24px;font-size:11px;color:#fff;padding-left:17px;position:relative;border-bottom:1px solid rgba(255,255,255,.28)}
.featured li:last-child{border-bottom:none}
.featured li::before{content:"";position:absolute;left:2px;top:9px;border-left:4px solid rgba(255,255,255,.8);border-top:3px solid transparent;border-bottom:3px solid transparent}

/* sidebar shade */
.sidebar-bg{left:579px;top:448px;width:284px;height:568px;background:linear-gradient(90deg,#f1f1f1,#fafafa 40%,#fff)}

/* welcome */
.welcome-title{left:23px;top:476px;font-size:16px}
.welcome-text{left:23px;top:504px;width:550px;font-size:9.5px;line-height:16px;color:#111;letter-spacing:-.1px}
.welcome-text p+p{margin-top:16px}
.welcome-text p.tight{margin-top:0}

/* projects */
.projects-title{left:21px;top:717px;font-size:16px}
.projects-rule{left:21px;top:744px;width:544px;height:1px;background:#ddd}
.project{top:745px;width:186px;height:250px}
.project-divider{top:745px;width:1px;height:248px;background:#e2e2e2}
.project-thumb{position:absolute;left:1px;top:11px;width:154px;height:68px;border:2px solid #d8d8d8}
.project h3{position:absolute;left:1px;top:89px;font-size:10.5px;font-weight:600;color:#111}
.project p{position:absolute;left:1px;top:106px;width:162px;font-size:9.1px;line-height:13.6px;color:#333}
.btn-more{position:absolute;left:0;width:70px;height:19px;background:#e4e4e4;border-radius:2px;font-size:8.5px;color:#111;display:flex;align-items:center;justify-content:center;letter-spacing:.2px}

/* video */
.video-title{left:597px;top:473px;font-size:16px}
.video-frame{left:595px;top:500px;width:242px;height:163px;background:#e3e3e3;box-shadow:0 4px 6px rgba(0,0,0,.12)}
.video-screen{position:absolute;left:8px;top:7px;width:226px;height:150px;background:#060606;border-radius:3px}

/* news */
.news-title{left:599px;top:686px;font-size:16px}
.news-item{left:600px;width:242px}
.news-date{font-size:10.5px;font-weight:700;color:#111}
.news-text{font-size:9.1px;line-height:15.3px;color:#333;margin-top:4px}
.news-meta{font-size:9.5px;font-weight:700;color:#222;margin-top:6px}
.news-meta span{font-weight:400;margin:0 6px}
.view-all{left:602px;top:962px;width:241px;height:23px;background:#0b0b0b;border-radius:2px;color:#fff;font-size:10.5px;text-align:right;padding-right:14px;line-height:23px;letter-spacing:.2px}

/* footer */
.footer{left:0;top:1016px;width:863px;height:144px;background:var(--footer)}
.footer-logo{left:30px;top:1048px}
.footer-logo .logo-name{color:#8a8a8a}
.footer-logo .logo-tag{color:#666}
.footer-heading{top:1038px;font-size:13px;color:#fff}
.footer-rule{top:1059px;height:1px;background:#4d4d4d}
.footer-label{left:315px;font-size:10.5px;color:#fff}
.footer-value{left:373px;font-size:10px;line-height:15px;color:var(--footer-text)}
.footer-note{left:533px;top:1068px;font-size:10.5px;color:var(--footer-text)}
.social{top:1090px;width:17px;height:17px;border-radius:3px;background:#3f7fc6}
.legal-bar{left:0;top:1160px;width:863px;height:40px;background:var(--footer-base)}
.legal{right:35px;top:1172px;font-size:10px;color:var(--footer-text)}
.legal span{margin:0 7px;color:#777}
</style>
</head>
<body>

<div class="abs top-strip"></div>
<header class="abs header"></header>

<div class="abs member-label">Member</div>
<div class="abs member-btn" style="left:702px;width:40px">Login</div>
<div class="abs member-btn" style="left:756px;width:53px">Sign Up</div>

<div class="abs logo">
  <div class="logo-name">Vela Errands</div>
  <div class="logo-tag">we make life easier</div>
</div>

<nav class="nav">
  <a class="active" href="#" style="left:358px">Home</a>
  <a href="#" style="left:450px">News</a>
  <a href="#" style="left:521px">About us</a>
  <a href="#" style="left:612px">Login</a>
  <a href="#" style="left:684px">Register</a>
  <a href="#" style="left:770px">Partners</a>
</nav>

<aside class="abs ad-banner">
  <div class="ad-fill" role="img" aria-label="Advertising banner space"></div>
</aside>

<div class="abs hero-photo" role="img" aria-label="Group of smiling concierge staff in suits standing in a hotel lobby"></div>
<section class="abs featured">
  <h2>Featured Services</h2>
  <ul>
    <li>Concierge First Services here</li>
    <li>Concierge Second Services</li>
    <li>Concierge third Services</li>
    <li>Concierge Fourth Services</li>
    <li>Concierge First Services here</li>
    <li>Concierge Second Services</li>
  </ul>
</section>

<div class="abs sidebar-bg"></div>

<h1 class="abs heading welcome-title">Welcome to Our Website Mainpage</h1>
<div class="abs welcome-text">
  <p>Brightline Web Studio is a web service company, offering a wide range of services which range from designing and development, that is covering almost all the fields in the best possible way. To be the best we know what and how to present beautifully the working of the client’s need and their advantages be highlighted. We act in accordance with the Industry certified processes to deliver the best to our clients all over the world. Over years we have built a strong reputation in providing website design and web development services.</p>
  <p>Thus, Wanna get ahead in the competition with other websites…. Brightline Web Studio provide you with an attractive and most convincing website to enhance your marketing goals.</p>
  <p class="tight">The only way to success is through the right path and that’s what we provide you. None of the other companies has the result we do. So stick to the best that’s how you will be the best don’t opt for the second best. Our expertise does not limit itself to web development but also it includes Web Hosting, Search Engine Optimization.</p>
</div>

<h2 class="abs heading projects-title">Featured Projects &amp; Reports</h2>
<div class="abs projects-rule"></div>

<article class="abs project" style="left:22px">
  <div class="project-thumb" role="img" aria-label="Close-up of banknotes and a pocket watch in blue tones" style="background:linear-gradient(135deg,#cfe3f7,#4f8fd0 55%,#dbe9f6)"></div>
  <h3>Headline Project Name</h3>
  <p>So that the website can achieve top position and ranking in the Internet searches and thereby increasing the scope for the website to be found by customers.<br>We here modify the site to improve the ranking by using the keywords and contents.</p>
  <div class="btn-more" style="top:223px">READ MORE</div>
</article>
<div class="abs project-divider" style="left:191px"></div>

<article class="abs project" style="left:208px">
  <div class="project-thumb" role="img" aria-label="Two business colleagues smiling in an office" style="background:linear-gradient(135deg,#e9eef3,#5b6f86 50%,#f0ece8)"></div>
  <h3>Headline Project Name</h3>
  <p>So that the website can achieve top position and ranking in the Internet searches and thereby increasing the scope for the website to be found by customers.<br>We here modify the site to improve the ranking by using the keywords and contents.</p>
  <div class="btn-more" style="top:224px">READ MORE</div>
</article>
<div class="abs project-divider" style="left:377px"></div>

<article class="abs project" style="left:394px">
  <div class="project-thumb" role="img" aria-label="Business team meeting around a laptop" style="background:linear-gradient(135deg,#d6d6d6,#5c5c5c 50%,#e4e4e4)"></div>
  <h3>Headline Project Name</h3>
  <p>So that the website can achieve top position and ranking in the Internet searches and thereby increasing the scope for the website to be found by customers.<br>We here modify the site to improve the ranking by using the keywords and contents.</p>
  <div class="btn-more" style="top:222px">READ MORE</div>
</article>

<h2 class="abs heading video-title">Watch Our Video</h2>
<div class="abs video-frame">
  <div class="video-screen">
    <svg width="226" height="150" viewBox="0 0 226 150" aria-label="Play video">
      <polygon points="104,59 104,97 134,78" fill="#fff"/>
    </svg>
  </div>
</div>

<h2 class="abs heading news-title">Latest News</h2>
<div class="abs news-item" style="top:718px">
  <div class="news-date">20.March.2012</div>
  <div class="news-text">Brightline Web Studio provides you the Search Engine Optimization making your website search engine friendly. So that the website can achieve top position and ranking</div>
  <div class="news-meta">READ MORE<span>|</span><b style="font-weight:600">2 hour ago</b></div>
</div>
<div class="abs news-item" style="top:838px">
  <div class="news-date">20.March.2012</div>
  <div class="news-text">Brightline Web Studio provides you the Search Engine Optimization making your website search engine friendly. So that the website can achieve top position and ranking</div>
  <div class="news-meta">READ MORE<span>|</span><b style="font-weight:600">2 hour ago</b></div>
</div>
<div class="abs view-all">VIEW ALL NEWS</div>

<footer class="abs footer"></footer>
<div class="abs footer-logo">
  <div class="logo-name">Vela Errands</div>
  <div class="logo-tag">we make life easier</div>
</div>

<div class="abs footer-heading" style="left:315px">Contact Info</div>
<div class="abs footer-rule" style="left:315px;width:194px"></div>
<div class="abs footer-label" style="top:1071px">Address:</div>
<div class="abs footer-value" style="top:1071px">44 Harbor Lane Street,<br>Springfield US</div>
<div class="abs footer-label" style="top:1106px">Phone no:</div>
<div class="abs footer-value" style="top:1106px">555-010-2841<br>555-010-7734</div>

<div class="abs footer-heading" style="left:533px">Stay In Touch</div>
<div class="abs footer-rule" style="left:533px;width:165px"></div>
<div class="abs footer-note">Find out what happening:</div>
<div class="abs social" style="left:533px;background:#3a9ee0" aria-label="Social link"></div>
<div class="abs social" style="left:553px;background:#2d78b8" aria-label="Social link"></div>
<div class="abs social" style="left:573px;background:#3b5e9c" aria-label="Social link"></div>

<div class="abs legal-bar"></div>
<div class="abs legal">Terms &amp; conditions<span>|</span>Privacy Policy<span>|</span>Site map</div>

</body>
</html>
```